KRMTOP - Harwell Clerical Solutions, Inc./Pinecrest Mailing Works, Inc. Needs a Letterhead Desig

Letterhead - thoughts 2 files uploaded 1 is the current letterhead and only change to the words is message at bottom - should be 25 Years of Industry Experience

2nd file is so that you can see how top of letterhead was before changes - had graphic bleed which we liked.

Goal for letterhead - we're a print / mail shop so we need a look that fits with agencies. I would like a bit of a square font for address, phone, email info otherwise be creative. We like a blue 307 and would like to incorporate a little green or tan.

```html
<!DOCTYPE html>
<html lang="en">
<head>
<meta charset="utf-8">
<title>KRMTOP Letterhead</title>
<link href="https://fonts.googleapis.com/css2?family=Tenor+Sans&display=swap" rel="stylesheet">
<style>
  :root {
    --blue-307: #1b62a8;
    --tan: #d2aa7c;
    --band-grey: #9a9b9e;
    --paper: #ffffff;
    --backdrop: #e9e7e3;
    --band-text: #f4f4f4;
  }
  html, body {
    margin: 0;
    width: 1200px;
    height: 1000px;
    overflow: hidden;
    background: var(--backdrop);
    font-family: "Tenor Sans", sans-serif;
  }
  .letterhead {
    position: absolute;
    left: 236px;
    top: 30px;
    width: 728px;
    height: 940px;
    background: var(--paper);
    box-shadow: 0 2px 10px rgba(0,0,0,0.12);
  }
  .masthead {
    position: absolute;
    right: 30px;
    top: 34px;
    display: flex;
    gap: 30px;
    align-items: flex-end;
  }
  .brand {
    display: flex;
    flex-direction: column;
    align-items: flex-start;
    color: var(--blue-307);
  }
  .brand-name {
    font-size: 26px;
    letter-spacing: 1px;
    line-height: 1;
  }
  .brand-legal {
    font-size: 7.5px;
    letter-spacing: 0.6px;
    text-transform: uppercase;
    margin-top: 3px;
    white-space: nowrap;
  }
  .header-rule {
    position: absolute;
    left: 0;
    right: 0;
    top: 82px;
    height: 2px;
    background: var(--tan);
  }
  .footer {
    position: absolute;
    left: 0;
    right: 0;
    bottom: 0;
  }
  .tagline-band {
    height: 22px;
    background: var(--band-grey);
    color: var(--band-text);
    font-size: 11px;
    letter-spacing: 1.2px;
    text-transform: uppercase;
    display: flex;
    align-items: center;
    justify-content: center;
  }
  .contact-line {
    height: 30px;
    padding: 0 16px;
    color: var(--blue-307);
    font-size: 9.5px;
    letter-spacing: 0.5px;
    text-transform: uppercase;
    display: flex;
    align-items: center;
    justify-content: center;
    gap: 8px;
    white-space: nowrap;
  }
  .contact-line .sep { font-size: 8px; }
  .base-band {
    height: 20px;
    background: var(--band-grey);
  }
</style>
</head>
<body>
  <div class="letterhead">
    <header class="masthead">
      <div class="brand">
        <span class="brand-name">Harwell</span>
        <span class="brand-legal">Harwell Clerical Solutions, Inc.</span>
      </div>
      <div class="brand">
        <span class="brand-name">Pinecrest</span>
        <span class="brand-legal">Pinecrest Mailing Works, Inc.</span>
      </div>
    </header>
    <div class="header-rule"></div>

    <footer class="footer">
      <div class="tagline-band">25 Years of Industry Experience</div>
      <div class="contact-line">
        <span>4120 W. Alder Row</span><span class="sep">&#8226;</span>
        <span>Millbrook, IL 60499</span><span class="sep">&#8226;</span>
        <span>Ph: 555-014-2280</span><span class="sep">&#8226;</span>
        <span>Fax: 555-014-2291</span><span class="sep">&#8226;</span>
        <span>Email: customerservice@krmtop.com</span>
      </div>
      <div class="base-band"></div>
    </footer>
  </div>
</body>
</html>
```